Responsive HomePage and InnerPage Design and HTML/CSS/JS Needed for the AI/Data Analysis Industry

I have an existing website and I am looking to redesign the HTML and layout of the homepage and menu to look more polished and robust. The website's existing homepage is at https://trelvonquip.com. The finished HTML/CSS/JS deliverable should be responsive down to mobile and include my new logo and a YouTube video to open in a modal window. It should look very professional and polished using the existing menu infrastructure. The color scheme and NEXA font should be used for all submitted designs should follow the attached branding guidelines.

Target Market(s)

Data Analytics Professionals and Users

Industry/Entity Type

AI/Data Analysis

Coding

Coded - Design and coding required

Number of Pages Required

2 page

Font styles to use
Other font styles liked:
• NEXA PRO

Requirements
Must have
• Responsiveness for large screens down to tablet and cell phone and follow the guidelines in the branding document provided.
Nice to have
• High converting design
Should not have
• Lots of whitespace in the design; Unresponsiveness; Poor Color Scheme that doesn't follow branding guide provided

```html
<!DOCTYPE html>
<html lang="en">
<head>
<meta charset="UTF-8">
<title>Trelvonquip – AI Log Analysis</title>
<link href="https://fonts.googleapis.com/css2?family=Montserrat:wght@400;500;600;700;800&display=swap" rel="stylesheet">
<style>
:root{
  --navy:#0a1240;
  --navy-deep:#070b2a;
  --band:#0c0f33;
  --orange:#e8552b;
  --orange-dark:#d2461f;
  --white:#ffffff;
  --ink:#1a1a1a;
  --muted:#555a66;
  --black:#000000;
  --line:rgba(255,255,255,.35);
}
*{box-sizing:border-box;margin:0;padding:0}
html,body{width:1200px;height:4020px;overflow:hidden}
body{font-family:"Montserrat",sans-serif;color:var(--ink);background:var(--white);position:relative}
a{color:inherit;text-decoration:none}

/* brand */
.brand{display:flex;align-items:center;gap:12px;color:var(--white);font-weight:700;font-size:22px;letter-spacing:.5px}
.brand-dot{width:22px;height:22px;border-radius:50%;background:var(--white)}

.btn{display:inline-block;background:var(--orange);color:var(--white);font-weight:600;border-radius:24px;padding:12px 30px;font-size:16px}

/* hero */
.hero{position:absolute;top:0;left:0;width:1200px;height:790px;overflow:hidden}
.hero-art{position:absolute;inset:0;background:
  radial-gradient(ellipse 420px 340px at 960px 360px,#3b6fd8 0%,rgba(40,80,200,.35) 45%,transparent 75%),
  radial-gradient(ellipse 300px 260px at 180px 300px,#1d3a9a 0%,transparent 70%),
  radial-gradient(ellipse 500px 200px at 420px 640px,rgba(232,85,43,.45) 0%,transparent 70%),
  linear-gradient(180deg,#0b1650 0%,#0a1240 60%,#1a1546 100%)}
.nav{position:absolute;top:0;left:0;right:0;height:80px;display:flex;align-items:center;padding:0 40px 0 130px}
.nav .brand{font-size:20px}
.nav-links{display:flex;gap:34px;margin-left:auto;margin-right:40px;list-style:none;color:var(--white);font-size:13px;font-weight:600}
.nav .btn{padding:12px 26px;font-size:15px}
.hero-copy{position:absolute;top:220px;left:0;width:1200px;text-align:center;color:var(--white)}
.hero-kicker{font-size:32px;font-weight:700;letter-spacing:1px}
.hero-title{font-size:64px;font-weight:800;letter-spacing:2px;margin-top:6px}
.hero-text{width:720px;margin:18px auto 0;font-size:17px;line-height:1.6;font-weight:500}
.hero-copy .btn{margin-top:28px}
.hero-wave{position:absolute;bottom:0;left:0}

/* about */
.about{position:absolute;top:790px;left:0;width:1200px;height:560px}
.about-art{position:absolute;left:80px;top:20px;width:480px;height:470px;border-radius:6px;background:
  radial-gradient(circle at 60% 40%,#e96d7d 0%,transparent 40%),
  radial-gradient(circle at 35% 70%,#4d55d6 0%,transparent 50%),
  linear-gradient(135deg,#1b1d5a,#8a2f7a 55%,#243a9c)}
.about-copy{position:absolute;left:600px;top:40px;width:520px}
.section-title{font-size:42px;font-weight:700;letter-spacing:2px;color:var(--ink)}
.about-copy p{margin-top:22px;font-size:15px;line-height:1.75;color:var(--muted)}
.about-copy .btn{margin-top:26px}

/* mission */
.mission{position:absolute;top:1370px;left:0;width:1200px;height:460px;background:var(--band);overflow:hidden}
.mission-art{position:absolute;right:0;top:0;width:680px;height:460px;background:
  radial-gradient(ellipse 260px 220px at 380px 220px,#3e8ff0 0%,rgba(40,100,220,.4) 45%,transparent 75%),
  linear-gradient(90deg,var(--band),#0e1a55)}
.mission-copy{position:absolute;left:110px;top:60px;width:450px;color:var(--white)}
.mv-head{display:flex;align-items:center;gap:12px;font-size:26px;font-weight:700}
.mv-head svg{flex:none}
.mission-copy p{margin-top:14px;font-size:15px;line-height:1.65}
.mv-block+.mv-block{margin-top:30px}

/* analyze */
.analyze{position:absolute;top:1830px;left:0;width:1200px;height:440px;text-align:center}
.analyze .section-title{margin-top:62px}
.cards{position:absolute;top:130px;left:132px;display:flex;gap:24px}
.card{position:relative;width:456px;height:280px;border-radius:10px;overflow:hidden}
.card-file{background:radial-gradient(circle at 50% 45%,#5ac4ff 0%,#1e4fb0 45%,#0a1850 100%)}
.card-interactive{background:radial-gradient(circle at 40% 40%,#5b7fd0 0%,#283870 50%,#121a3c 100%)}
.card .btn{position:absolute;left:50%;bottom:14px;transform:translateX(-50%);border-radius:4px;width:360px;font-size:18px;padding:12px 0}

/* faq */
.faq{position:absolute;top:2270px;left:0;width:1200px;height:800px;text-align:center}
.faq .section-title{margin-top:40px}
.faq-list{position:absolute;top:130px;left:180px;width:840px;list-style:none;text-align:left}
.faq-item{background:var(--white);box-shadow:0 2px 8px rgba(0,0,0,.18);margin-bottom:6px;padding:0 22px;font-size:15px;font-weight:600}
.faq-q{height:48px;display:flex;align-items:center;justify-content:space-between}
.faq-a{font-size:13px;font-weight:400;color:var(--muted);line-height:1.6;padding:0 30px 14px 0;border-top:1px solid #ddd;padding-top:10px}
.faq-icon{width:11px;height:11px;background:var(--ink);transform:rotate(45deg)}
.faq-minus{width:14px;height:2px;background:var(--ink)}

/* contact */
.contact{position:absolute;top:3100px;left:0;width:1200px;height:480px;background:var(--navy-deep);overflow:hidden}
.contact-art{position:absolute;left:0;top:0;width:560px;height:480px;background:
  radial-gradient(ellipse 200px 260px at 260px 260px,#3a6fd6 0%,rgba(40,80,200,.35) 50%,transparent 80%),
  radial-gradient(ellipse 160px 120px at 120px 380px,rgba(232,85,43,.5) 0%,transparent 70%),
  linear-gradient(90deg,#0b1650,var(--navy-deep))}
.contact-form{position:absolute;left:552px;top:40px;width:530px}
.contact-form .section-title{color:var(--white);text-align:center;margin-bottom:26px}
.row{display:flex;gap:20px;margin-bottom:16px}
.field{flex:1;height:44px;border:1px solid var(--white);border-radius:6px;color:var(--white);font-size:13px;padding:12px 14px}
.field-msg{height:130px}
.contact-form .submit{display:inline-block;margin-top:6px;background:var(--white);color:var(--ink);font-weight:600;border-radius:22px;padding:12px 40px;font-size:15px}

/* footer */
.footer{position:absolute;top:3580px;left:0;width:1200px;height:440px;background:var(--black);color:var(--white)}
.footer .brand{position:absolute;left:120px;top:110px;font-size:24px}
.f-col{position:absolute;top:70px}
.f-col h4{font-size:22px;font-weight:700;margin-bottom:18px}
.f-col ul{list-style:none;font-size:13px;line-height:2}
.f-main{left:400px}.f-other{left:640px}.f-follow{left:880px}
.socials{display:flex;gap:14px}
.socials span{width:30px;height:30px;border:1.5px solid var(--white);border-radius:50%}
.f-rule{position:absolute;left:120px;right:120px;top:300px;height:1px;background:var(--line)}
.copyright{position:absolute;top:320px;left:0;width:1200px;text-align:center;font-size:13px}
</style>
</head>
<body>

<header class="hero">
  <div class="hero-art" role="img" aria-label="Glowing blue digital human profile made of light particles on a dark navy background"></div>
  <nav class="nav">
    <a class="brand" href="https://trelvonquip.com"><span class="brand-dot"></span>Trelvonquip</a>
    <ul class="nav-links"><li>HOME</li><li>ANALYZE LOG FILES</li><li>ABOUT US</li><li>FAQ</li><li>CONTACT US</li></ul>
    <a class="btn" href="#">Get Started</a>
  </nav>
  <div class="hero-copy">
    <div class="hero-kicker">WELCOME TO</div>
    <h1 class="hero-title">TRELVONQUIP</h1>
    <p class="hero-text">Artificial intelligence (AI) has transformed the world in many remarkable ways. Among the latest innovations is Generative AI, which represents a new era of possibility in data analysis and processing.</p>
    <a class="btn" href="#">Read More</a>
  </div>
  <svg class="hero-wave" width="1200" height="120" viewBox="0 0 1200 120" aria-hidden="true"><path d="M0 70 C300 130 700 130 1000 60 C1090 40 1160 30 1200 20 L1200 120 L0 120Z" fill="#ffffff"/></svg>
</header>

<section class="about">
  <div class="about-art" role="img" aria-label="Hands typing on a laptop surrounded by colourful glowing data streams"></div>
  <div class="about-copy">
    <h2 class="section-title">ABOUT US</h2>
    <p>Meet our founder, Dorin Vale: a passionate data analyst who has spent his entire career unraveling the complex mysteries hidden within data. Dorin's journey in data analysis was sparked by an early fascination with the infinite possibilities of data interpretation. He realized the enormous potential of transforming raw, seemingly chaotic data into meaningful information that can drive decision-making processes and strategies. With this conviction, he channeled</p>
    <a class="btn" href="#">Read More</a>
  </div>
</section>

<section class="mission">
  <div class="mission-art" role="img" aria-label="Glowing blue circuit brain with network lines"></div>
  <div class="mission-copy">
    <div class="mv-block">
      <h3 class="mv-head"><svg width="30" height="30" viewBox="0 0 30 30"><circle cx="15" cy="15" r="13" fill="none" stroke="#fff" stroke-width="2"/><circle cx="15" cy="15" r="7" fill="none" stroke="#fff" stroke-width="2"/><circle cx="15" cy="15" r="2.5" fill="#fff"/></svg>OUR MISSION</h3>
      <p>Our mission is to revolutionize log analysis using cutting-edge Generative AI, simplifying the extraction of meaningful insights from diverse log formats. We aim to empower developers, IT professionals, and data analysts by providing a seamless tool that effortlessly identifies trends, spots anomalies, and predicts potential issues.</p>
    </div>
    <div class="mv-block">
      <h3 class="mv-head"><svg width="30" height="30" viewBox="0 0 30 30"><path d="M2 15 Q15 3 28 15 Q15 27 2 15Z" fill="none" stroke="#fff" stroke-width="2"/><circle cx="15" cy="15" r="4" fill="#fff"/></svg>OUR VISION</h3>
      <p>Our vision is to be the forefront provider, enabling organizations to make informed decisions, proactively address challenges, and optimize system performance through advanced log analysis solutions.</p>
    </div>
  </div>
</section>

<section class="analyze">
  <h2 class="section-title">ANALYZE LOGS</h2>
  <div class="cards">
    <div class="card card-file" role="img" aria-label="Glowing cloud above a circuit board representing file upload">
      <a class="btn" href="#">Standard File Analysis</a>
    </div>
    <div class="card card-interactive" role="img" aria-label="Analyst working at a computer with charts on screen">
      <a class="btn" href="#">Interactive File Analysis</a>
    </div>
  </div>
</section>

<section class="faq">
  <h2 class="section-title">FREQUENTLY ASKED QUESTION</h2>
  <ul class="faq-list">
    <li class="faq-item"><div class="faq-q">What is Trelvonquip?<span class="faq-icon"></span></div></li>
    <li class="faq-item"><div class="faq-q">Which file formats does Trelvonquip support?<span class="faq-icon"></span></div></li>
    <li class="faq-item"><div class="faq-q">How does Trelvonquip analyze log files?<span class="faq-icon"></span></div></li>
    <li class="faq-item"><div class="faq-q">Is it safe and secure to use Trelvonquip?<span class="faq-minus"></span></div>
      <p class="faq-a">Yes, using Trelvonquip is completely safe and secure. We do not upload your files to our servers. Our system analyzes the data directly from the files on your device, ensuring that your sensitive information remains private and secure.</p></li>
    <li class="faq-item"><div class="faq-q">How do I use Trelvonquip?<span class="faq-icon"></span></div></li>
    <li class="faq-item"><div class="faq-q">Do you store any of my data?<span class="faq-icon"></span></div></li>
    <li class="faq-item"><div class="faq-q">Can Trelvonquip handle large files?<span class="faq-icon"></span></div></li>
    <li class="faq-item"><div class="faq-q">What kind of insights can I expect from Trelvonquip?<span class="faq-icon"></span></div></li>
    <li class="faq-item"><div class="faq-q">Who can benefit from using Trelvonquip?<span class="faq-icon"></span></div></li>
    <li class="faq-item"><div class="faq-q">Is there customer support available for Trelvonquip?<span class="faq-icon"></span></div></li>
  </ul>
</section>

<section class="contact">
  <div class="contact-art" role="img" aria-label="Glowing humanoid robot reaching toward a digital interface"></div>
  <div class="contact-form">
    <h2 class="section-title">CONTACT US</h2>
    <div class="row"><div class="field">First Name</div><div class="field">Last Name</div></div>
    <div class="row"><div class="field">Email Address</div><div class="field">Phone Number</div></div>
    <div class="row"><div class="field field-msg">Your Message</div></div>
    <a class="submit" href="#">Submit</a>
  </div>
</section>

<footer class="footer">
  <a class="brand" href="https://trelvonquip.com"><span class="brand-dot"></span>Trelvonquip</a>
  <div class="f-col f-main"><h4>Main Links</h4><ul><li>Home</li><li>Analyze Log Files</li><li>About Us</li><li>FAQ</li><li>Contact Us</li></ul></div>
  <div class="f-col f-other"><h4>Other Links</h4><ul><li>Terms and conditions</li><li>Privacy Policy</li><li>Career</li></ul></div>
  <div class="f-col f-follow"><h4>Follow Us</h4><div class="socials"><span></span><span></span><span></span></div></div>
  <div class="f-rule"></div>
  <p class="copyright">2024 Copyright ©, Trelvonquip | All Rights Reserved</p>
</footer>

</body>
</html>
```